Acupuncture business needs business card design

I need a business card for an acupuncture clinic called "Harbour Balance"
It will need the following details:
My name: Mark Tevita
Acupuncturist
Member KPTG
WFB Treatment Provider
Ph numbers: 512 8830 027 584 1176
Email: mark@hbneedle.example.nz
On the back it will need a table with 2 columns for appointments, one column for time and one for date.

Industry/Entity Type

Clinic

Contact Information for Business Card

Mark Tevita
Acupuncturist
Member KPTG
WFB Treatment Provider
Email: mark@hbneedle.example.nz

Requirements
Must have
• Mark Tevita
• Acupuncturist
• Member KPTG
• WFB Treatment Provider
• Ph numbers: 512 8830 027 584 1176
• Email: mark@hbneedle.example.nz
• On the back it will need a table with 2 columns for appointments, one column for time and one for date.

```html
<!DOCTYPE html>
<html lang="en">
<head>
<meta charset="utf-8">
<title>Harbour Balance – Business Card</title>
<link href="https://fonts.googleapis.com/css2?family=Open+Sans:ital,wght@0,400;0,600;0,700;1,300&display=swap" rel="stylesheet">
<style>
  :root {
    --teal: #127a92;
    --sky: #0ab0e0;
    --white: #ffffff;
    --backdrop: #e2e2e2;
    --rule: rgba(255,255,255,0.85);
  }
  html, body {
    margin: 0;
    padding: 0;
    width: 1006px;
    height: 1200px;
    overflow: hidden;
    background: var(--backdrop);
    font-family: "Open Sans", sans-serif;
  }
  .stage {
    position: absolute;
    left: 0;
    top: 0;
    width: 1200px;
    height: 1430px;
    transform: scale(0.8383);
    transform-origin: 0 0;
    background: radial-gradient(ellipse at center, #f2f2f2 0%, var(--backdrop) 75%);
  }
  .card {
    position: absolute;
    left: 95px;
    width: 1010px;
    height: 624px;
    overflow: hidden;
  }
  .card--front { top: 87px; background: var(--white); }
  .card--back { top: 718px; height: 625px; background: var(--teal); }
  .card__wave { position: absolute; left: 0; top: 0; }
  .txt { position: absolute; line-height: 1; white-space: nowrap; color: var(--white); }

  .brand__dot {
    position: absolute; left: 72px; top: 53px;
    width: 110px; height: 110px; border-radius: 50%;
    background: var(--teal);
  }
  .brand__name { left: 223px; top: 60px; font-size: 86px; font-weight: 600; color: var(--sky); letter-spacing: -1.5px; }
  .brand__tagline { left: 223px; top: 146px; font-size: 24px; font-weight: 400; color: var(--teal); letter-spacing: 0.52em; }

  .person__name { left: 158px; top: 287px; font-size: 50px; font-weight: 700; }
  .person__rule {
    position: absolute; left: 60px; top: 344px; width: 500px; height: 1px;
    background: linear-gradient(90deg, rgba(255,255,255,0), rgba(255,255,255,0.7) 40%, rgba(255,255,255,0));
  }
  .person__role { left: 161px; top: 351px; font-size: 38px; font-weight: 300; font-style: italic; }
  .person__member { left: 457px; top: 360px; font-size: 30px; font-weight: 700; }
  .contact__icon { position: absolute; }
  .contact__phone { left: 201px; top: 416px; font-size: 28px; font-weight: 700; }
  .contact__email { left: 199px; top: 464px; font-size: 26px; font-weight: 400; }
  .person__provider { left: 158px; top: 516px; font-size: 26px; font-weight: 700; }

  .appt__label { font-size: 32px; font-weight: 400; }
  .appt__label--appointments { left: 114px; top: 28px; }
  .appt__label--time { left: 111px; top: 325px; }
  .appt__label--date { left: 509px; top: 323px; }
  .appt__box {
    position: absolute; width: 389px; height: 233px;
    border: 1px solid var(--rule); box-sizing: border-box;
  }
</style>
</head>
<body>
<div class="stage">

  <section class="card card--front">
    <svg class="card__wave" width="1010" height="624" viewBox="0 0 1010 624" aria-hidden="true">
      <path d="M0,211 Q650,222 1010,418 L1010,624 L0,624 Z" fill="var(--sky)"/>
      <path d="M0,212 Q620,232 1010,458 L1010,624 L0,624 Z" fill="var(--teal)"/>
    </svg>

    <div class="brand__dot"></div>
    <div class="txt brand__name">Harbour Balance</div>
    <div class="txt brand__tagline">ACUPUNCTURE PHYSIOTHERAPY</div>

    <div class="txt person__name">Mark Tevita</div>
    <div class="person__rule"></div>
    <div class="txt person__role">Acupuncturist</div>
    <div class="txt person__member">Member KPTG</div>

    <svg class="contact__icon" style="left:159px;top:406px" width="22" height="44" viewBox="0 0 22 44" aria-hidden="true">
      <rect x="1" y="6" width="20" height="37" rx="2" fill="none" stroke="#fff" stroke-width="2"/>
      <line x1="17" y1="6" x2="17" y2="0" stroke="#fff" stroke-width="2"/>
      <rect x="4" y="10" width="14" height="8" fill="#fff"/>
      <path d="M4,22 H18 M4,27 H18 M4,32 H18 M4,37 H18 M8.5,22 V40 M13.5,22 V40" stroke="#fff" stroke-width="1.4"/>
    </svg>
    <div class="txt contact__phone">512 8830 027 584 1176</div>

    <svg class="contact__icon" style="left:154px;top:466px" width="32" height="24" viewBox="0 0 32 24" aria-hidden="true">
      <path d="M1,10 L16,1 L31,10 V23 H1 Z" fill="#fff"/>
      <path d="M1,10 L16,19 L31,10" fill="none" stroke="var(--teal)" stroke-width="2"/>
    </svg>
    <div class="txt contact__email">mark@hbneedle.example.nz</div>

    <div class="txt person__provider">WFB Treatment Provider</div>
  </section>

  <section class="card card--back">
    <div class="txt appt__label appt__label--appointments">Appointments</div>
    <div class="appt__box" style="left:111px;top:69px"></div>
    <div class="appt__box" style="left:511px;top:69px"></div>
    <div class="txt appt__label appt__label--time">Time</div>
    <div class="txt appt__label appt__label--date">Date</div>
    <div class="appt__box" style="left:111px;top:362px"></div>
    <div class="appt__box" style="left:511px;top:362px"></div>
  </section>

</div>
</body>
</html>
```